Orbit 582 - Kindle Book Cover

I am looking for a Kindle book cover for my book about "Orbit 582".
The Book is Titled:
Orbit 582 Ascended
Shaping Tomorrow: Paths To Unlocking Hidden Currents
Author is Dorian Welby
Here is a book description that may help you understand more about it:
Inspired by the genius of Bertram Ollinger, this comprehensive guide delves into the ancient wisdom and cutting-edge science behind the 582 method, a powerful tool for manifesting your desires. Whether you're seeking personal growth, financial success, or spiritual enlightenment, this book provides advanced techniques and methods to transform your dreams into reality.
Any questions please ask.
Thanks
Gavin

```html
<!DOCTYPE html>
<html lang="en">
<head>
<meta charset="utf-8">
<title>Orbit 582 Ascended — Dorian Welby</title>
<link rel="stylesheet" href="https://fonts.googleapis.com/css2?family=Montserrat:wght@800;900&family=Tinos:wght@400;700&family=Cinzel:wght@400&display=swap">
<style>
  :root {
    --night-deep: #140f33;
    --night-mid: #2a2160;
    --night-glow: #3e3580;
    --star: rgba(255, 255, 255, 0.55);
    --series-gold: #f6d98b;
    --numeral-ice: #e6f3fd;
    --label-white: #ffffff;
    --author-blush: #eed6cc;
    --ornament-core: rgba(235, 235, 255, 0.32);
    --ornament-edge: rgba(180, 175, 230, 0.0);
  }
  html, body {
    margin: 0;
    padding: 0;
    overflow: hidden;
    background: var(--night-deep);
  }
  .cover {
    position: relative;
    width: 805px;
    height: 1200px;
    overflow: hidden;
    background:
      radial-gradient(1px 1px at 12% 8%, var(--star), transparent 60%),
      radial-gradient(1px 1px at 34% 4%, var(--star), transparent 60%),
      radial-gradient(1.5px 1.5px at 58% 12%, var(--star), transparent 60%),
      radial-gradient(1px 1px at 77% 6%, var(--star), transparent 60%),
      radial-gradient(1px 1px at 22% 22%, var(--star), transparent 60%),
      radial-gradient(1.5px 1.5px at 88% 28%, var(--star), transparent 60%),
      radial-gradient(1px 1px at 8% 40%, var(--star), transparent 60%),
      radial-gradient(1px 1px at 93% 52%, var(--star), transparent 60%),
      radial-gradient(1px 1px at 15% 66%, var(--star), transparent 60%),
      radial-gradient(1px 1px at 84% 74%, var(--star), transparent 60%),
      radial-gradient(ellipse 70% 30% at 30% 12%, rgba(120, 110, 190, 0.35), transparent 70%),
      linear-gradient(170deg, var(--night-glow) 0%, var(--night-mid) 35%, #211a4e 65%, var(--night-deep) 100%);
    font-family: "Montserrat", sans-serif;
  }
  .mandala {
    position: absolute;
    left: 155px;
    top: 258px;
    width: 520px;
    height: 550px;
  }
  .title {
    position: absolute;
    left: 0;
    top: 0;
    margin: 0;
    width: 100%;
    font-weight: 800;
  }
  .title-series {
    position: absolute;
    left: 160px;
    top: 354px;
    font-size: 50px;
    line-height: 1;
    letter-spacing: -1px;
    color: var(--series-gold);
    text-shadow: 3px 4px 0 rgba(20, 15, 50, 0.6);
  }
  .title-numeral {
    position: absolute;
    left: 0;
    width: 100%;
    top: 385px;
    text-align: center;
    padding-left: 10px;
    box-sizing: border-box;
    font-size: 262px;
    line-height: 1;
    letter-spacing: -14px;
    font-weight: 900;
    color: var(--numeral-ice);
  }
  .title-edition {
    position: absolute;
    left: 0;
    width: 100%;
    top: 662px;
    text-align: center;
    padding-left: 10px;
    box-sizing: border-box;
    font-size: 53px;
    line-height: 1;
    letter-spacing: 22px;
    color: var(--label-white);
  }
  .subtitle {
    position: absolute;
    left: 0;
    width: 790px;
    top: 842px;
    margin: 0;
    text-align: center;
    font-family: "Tinos", serif;
    color: var(--label-white);
  }
  .subtitle-lead {
    display: block;
    font-weight: 700;
    font-size: 28px;
    line-height: 1.2;
    letter-spacing: -0.5px;
  }
  .subtitle-line {
    display: block;
    font-weight: 400;
    font-size: 27px;
    line-height: 1.18;
  }
  .author {
    position: absolute;
    left: 0;
    width: 805px;
    top: 1102px;
    margin: 0;
    text-align: center;
    font-family: "Cinzel", serif;
    font-weight: 400;
    font-size: 48px;
    letter-spacing: 20px;
    padding-left: 20px;
    box-sizing: border-box;
    color: var(--author-blush);
  }
</style>
</head>
<body>
  <main class="cover">
    <svg class="mandala" role="img" aria-label="Sacred geometry mandala illustration with radiating lines and rings" viewBox="0 0 520 550">
      <defs>
        <radialGradient id="mandalaGlow" cx="50%" cy="50%" r="50%">
          <stop offset="0%" stop-color="var(--ornament-core)"/>
          <stop offset="70%" stop-color="rgba(220,220,250,0.18)"/>
          <stop offset="100%" stop-color="var(--ornament-edge)"/>
        </radialGradient>
      </defs>
      <ellipse cx="260" cy="275" rx="260" ry="275" fill="url(#mandalaGlow)"/>
    </svg>

    <h1 class="title">
      <span class="title-series">ORBIT</span>
      <span class="title-numeral">582</span>
      <span class="title-edition">ASCENDED</span>
    </h1>

    <p class="subtitle">
      <span class="subtitle-lead">SHAPING TOMORROW:</span>
      <span class="subtitle-line">Paths to unlocking</span>
      <span class="subtitle-line">hidden currents</span>
    </p>

    <p class="author">DORIAN WELBY</p>
  </main>
</body>
</html>
```